Bref créative
Motorcycle/ATV repair Parts and accessories
Ridge Fold Cycles
Professional
Lon Perrick
4127 Mellow Lane
Brookvale, NC 28514
RFCgarage@ridgefoldcycles.example
www.RidgeFoldCycles.example
Business hours are M-F 9-6 Sat. 9-3 Closed Sun.
Parts and service for Motorcycle ATVs amd watercraft.
Anything creative!! Make it sound good! the logo is great and now we need the card to match it.

```html
<!DOCTYPE html>
<html lang="en">
<head>
<meta charset="utf-8">
<title>Ridge Fold Cycles – Business Card</title>
<link rel="stylesheet" href="https://fonts.googleapis.com/css2?family=Orbitron:wght@700&family=Michroma&display=swap">
<style>
  :root {
    --page: #d9d9d9;
    --card: #0d0d0d;
    --card-hi: #1e1e1e;
    --orange: #f2a51f;
    --orange-deep: #c9820f;
    --silver: #b9bcc0;
    --silver-dark: #6f7277;
    --text: #e6e6e6;
  }
  * { box-sizing: border-box; margin: 0; padding: 0; }
  html, body { width: 1200px; height: 864px; overflow: hidden; }
  body {
    background: var(--page);
    position: relative;
    font-family: "Michroma", "Helvetica Neue", Arial, sans-serif;
  }
  .card {
    position: absolute;
    top: 277px;
    width: 540px;
    height: 309px;
    border-radius: 18px;
    background: radial-gradient(ellipse at 50% 35%, var(--card-hi), var(--card) 70%);
    overflow: hidden;
  }
  .card--front { left: 40px; }
  .card--back { left: 620px; }

  .wordmark {
    position: absolute;
    font-family: "Orbitron", "Arial Black", sans-serif;
    font-weight: 700;
    color: var(--orange);
    text-transform: uppercase;
    letter-spacing: 1px;
    white-space: nowrap;
    display: flex;
    align-items: center;
    gap: 10px;
  }
  .wordmark__mark {
    width: 14px; height: 14px;
    background: var(--orange);
    flex: none;
  }
  .card--front .wordmark {
    left: 0; right: 0; top: 128px;
    justify-content: center;
    font-size: 30px;
  }
  .card--back .wordmark {
    left: 70px; top: 92px;
    font-size: 24px;
  }
  .holder {
    position: absolute;
    left: 212px; top: 150px;
    font-size: 8px;
    color: var(--orange);
    letter-spacing: 1px;
    text-transform: uppercase;
  }
  .address {
    position: absolute;
    right: 334px; top: 170px;
    text-align: right;
    font-size: 8px;
    line-height: 14px;
    color: var(--text);
    text-transform: uppercase;
    letter-spacing: 0.5px;
    white-space: nowrap;
  }
  .contacts {
    position: absolute;
    left: 218px; top: 166px;
    list-style: none;
    font-size: 7.5px;
    line-height: 14px;
    color: var(--text);
    text-transform: uppercase;
    letter-spacing: 0.4px;
    white-space: nowrap;
  }
  .contacts li { display: flex; align-items: center; gap: 6px; }
  .contacts__icon {
    width: 9px; height: 9px; border-radius: 50%;
    background: var(--orange); flex: none;
  }
  .divider {
    position: absolute;
    left: 212px; top: 166px;
    width: 1px; height: 56px;
    background: var(--orange);
  }
  .swoosh { position: absolute; inset: 0; width: 100%; height: 100%; }
</style>
</head>
<body>

<section class="card card--front" aria-label="Business card front">
  <div class="wordmark"><span class="wordmark__mark"></span>Ridge Fold Cycles</div>
</section>

<section class="card card--back" aria-label="Business card back">
  <svg class="swoosh" viewBox="0 0 540 309" aria-hidden="true">
    <defs>
      <linearGradient id="silverBand" x1="0" y1="0" x2="1" y2="0">
        <stop offset="0" stop-color="#6f7277"/>
        <stop offset="0.6" stop-color="#b9bcc0"/>
        <stop offset="1" stop-color="#e2e4e6"/>
      </linearGradient>
      <linearGradient id="orangeBand" x1="0" y1="0" x2="1" y2="0">
        <stop offset="0" stop-color="#c9820f"/>
        <stop offset="1" stop-color="#f2a51f"/>
      </linearGradient>
    </defs>
    <path d="M250 309 C360 290 470 250 540 150 L540 190 C480 265 390 300 300 309 Z" fill="url(#silverBand)"/>
    <path d="M320 309 C420 295 500 250 540 205 L540 309 Z" fill="url(#orangeBand)"/>
  </svg>

  <div class="wordmark"><span class="wordmark__mark"></span>Ridge Fold Cycles</div>
  <p class="holder">Lon Perrick</p>
  <p class="address">4127 Mellow Lane<br>Brookvale<br>NC 28514</p>
  <span class="divider"></span>
  <ul class="contacts">
    <li><span class="contacts__icon"></span>(919) 555-0142</li>
    <li><span class="contacts__icon"></span>RFCgarage@ridgefoldcycles.example</li>
    <li><span class="contacts__icon"></span>www.RidgeFoldCycles.example</li>
  </ul>
</section>

</body>
</html>
```